Futuristic and Visually Appealing Photo Booth Rental Website

I need a Photo Booth rental website made for easy editing through Wordpress. Web design + Page Templates are needed for showcasing booths, packages, experiences, and add-ons. There's a space and futuristic theme to the company that I'd like to stick with. I'd like to integrate certain parts of the site with html code (iframe) but others with text, pictures, and video. I'd like the design as complete as possible while I help work on the content as much as I can. The priority should be making the site friendly enough to educate and convert sales/bookings. I have no problem working from a general photobooth website as a base.

Company: SnapNova QX

Coding required. All source files needed to install as theme that can be edited by something like Elementor.

**Contact for current design done under maintenance mode**

Target Market(s)

All consumers (holiday parties, birthdays, weddings, etc...)
Corporate Clients (conventions, virtual expos, holiday parties, company events)

Industry/Entity Type

Events

Coding

Coded - Design and coding required

Font styles to use
Sans Serif

Requirements
Must have
• ===Menu/Submenu===
Our Booths: DSLR Open Air Photo Booth, Selfie Station, Drifter, Pendulum Skimmer, LumiSpin
Consumers: Rental Packages, Addons
Corporate: Experiences, Addons, Build-to-Suit, Get a Quote (iframe)
About: About Us, Non-Profits, Employment
Customizations: Printout Templates (iframe), Start Screens (iframe), Backdrops
Contact Us: Inquiry, Custom Quote

===Buttons/Call to Action===
Book Online
Find My Photos
Client Portal

Social Media Icons and Footer section for vendor buttons (bridalloom, grumble, the veil, etc...)

Responsive design
Nice to have
• Video Slides on Frontpage
Should not have
• OnePage Design

```html
<!DOCTYPE html>
<html lang="en">
<head>
<meta charset="utf-8">
<title>SnapNova QX — Photo Booth Rentals</title>
<link rel="stylesheet" href="https://fonts.googleapis.com/css2?family=Roboto:wght@400;500;700&display=swap">
<style>
:root{
  --teal:#1ec6c6;
  --teal-dark:#14a9b0;
  --navy:#120f3d;
  --navy-deep:#0c0a2c;
  --purple:#2a1b6e;
  --card:#0f0c33;
  --white:#ffffff;
  --muted:#d9dcf2;
  --star:#ffc21a;
}
*{margin:0;padding:0;box-sizing:border-box}
html,body{width:1200px;height:3479px;overflow:hidden}
body{font-family:'Roboto',sans-serif;color:var(--white);background:var(--navy-deep);position:relative}
.abs{position:absolute}
.section-title{position:absolute;left:0;width:1200px;text-align:center;font-size:35px;font-weight:700;letter-spacing:.5px}

/* hero */
.hero{position:absolute;left:0;top:0;width:1200px;height:760px;background:linear-gradient(180deg,#1a1550 0%,#2a1e72 45%,#1d2c86 70%,#142061 100%)}
.hero-scene{position:absolute;left:0;top:180px;width:1200px;height:560px;background:linear-gradient(180deg,rgba(60,40,140,.0) 0%,rgba(90,50,170,.55) 35%,rgba(30,110,200,.45) 60%,rgba(20,40,120,.6) 100%)}
.hero-sun{position:absolute;left:450px;top:185px;width:300px;height:300px;border-radius:50%;background:radial-gradient(circle,#6a2bb4 0 48%,#ff6a3d 49% 60%,#ff3e8a 70%,rgba(255,62,138,0) 72%)}
.brand{position:absolute;display:flex;align-items:center;gap:10px;font-weight:700;color:var(--white)}
.brand-dot{border-radius:50%;border:3px solid var(--teal);background:var(--navy)}
.nav{position:absolute;top:76px;left:290px;display:flex;gap:17px;font-size:13px;font-weight:500}
.nav a{color:var(--white);text-decoration:none}
.nav a.active{color:var(--teal);border-bottom:2px solid var(--teal);padding-bottom:6px}
.btn-outline{position:absolute;border:2px solid var(--teal);border-radius:20px;color:var(--teal);font-size:14px;font-weight:500;display:flex;align-items:center;justify-content:center;gap:7px}
.btn-solid{position:absolute;background:var(--teal);border-radius:22px;color:var(--white);font-size:15px;font-weight:500;display:flex;align-items:center;justify-content:center;gap:8px}
.hero-text{position:absolute;top:455px;left:0;width:1200px;text-align:center;font-size:16px;line-height:27px;font-weight:500}

/* booths */
.booths{position:absolute;left:0;top:740px;width:1200px;height:590px;background:radial-gradient(ellipse at 80% 70%,#3a1f7a 0%,#1a1652 55%,#131040 100%)}
.booth{position:absolute;width:220px;text-align:center}
.booth-img{width:200px;height:200px;margin:0 auto;border-radius:50%;border:3px solid var(--teal);padding:8px}
.booth-img div{width:100%;height:100%;border-radius:50%}
.booth h3{font-size:17px;font-weight:700;margin-top:21px}
.booth p{font-size:14px;line-height:20px;margin-top:11px;color:var(--muted)}

/* targets */
.targets{position:absolute;left:0;top:1330px;width:1200px;height:540px;background:#110d37}
.target{position:absolute;width:320px}
.target h4{font-size:16px;font-weight:700;letter-spacing:.3px}
.target p{font-size:14px;line-height:22px;margin-top:11px;color:var(--muted)}
.target.left{text-align:right}
.t-icon{position:absolute;width:74px;height:74px;border-radius:50%;border:2px solid #9aa0d6}
.t-icon svg{position:absolute;left:21px;top:21px}

/* packages */
.packages{position:absolute;left:0;top:1870px;width:1200px;height:720px;background:linear-gradient(180deg,#161148 0%,#1c1656 100%)}
.pkg{position:absolute;top:2100px;width:310px;height:330px;background:var(--card);text-align:center}
.pkg h3{font-size:26px;font-weight:500;margin-top:26px}
.pkg p.desc{font-size:16px;line-height:23px;margin-top:12px;color:var(--muted)}
.pkg .price{font-size:34px;font-weight:700;color:var(--teal);margin-top:12px}
.pkg .per{font-size:16px;color:var(--muted)}
.pkg .feat{font-size:17px;margin-top:18px}
.pkg .try{display:inline-flex;align-items:center;justify-content:center;width:152px;height:48px;margin-top:22px;border:2px solid var(--teal);color:var(--teal);font-size:17px;font-weight:500}
.pkg .try.fill{background:var(--teal);color:var(--white)}
.popular{position:absolute;left:445px;top:2050px;width:310px;height:50px;background:var(--teal);font-size:20px;font-weight:500;display:flex;align-items:center;justify-content:center}

/* experiences */
.experiences{position:absolute;left:0;top:2560px;width:1200px;height:545px;background:linear-gradient(180deg,#1a2a85 0%,#146ea8 55%,#1688b0 100%)}
.review{position:absolute;top:2778px;width:310px;height:190px;background:var(--white);border-radius:10px;color:#333;text-align:center;font-size:13px;line-height:23px;padding:60px 26px 0}
.review::after{content:"";position:absolute;left:146px;bottom:-9px;border:9px solid transparent;border-bottom:0;border-top-color:var(--white)}
.avatar{position:absolute;width:92px;height:92px;border-radius:50%;border:3px solid var(--white);background:linear-gradient(160deg,#c9c4bf,#7c6a60)}
.reviewer{position:absolute;top:2990px;width:310px;text-align:center;font-size:15px;font-weight:500}
.stars{position:absolute;top:3012px;width:310px;text-align:center}

/* footer */
.footer{position:absolute;left:0;top:3105px;width:1200px;height:374px;background:#120e3e}
.f-head{position:absolute;top:3166px;font-size:19px;font-weight:500}
.f-text{position:absolute;font-size:14px;line-height:20px;color:var(--muted)}
.f-links{position:absolute;left:395px;top:3215px;font-size:14px;line-height:26.6px;color:var(--muted)}
.vendor{position:absolute;left:538px;font-weight:500;color:var(--teal);display:flex;align-items:center;gap:6px}
.social{position:absolute;top:3325px;width:32px;height:32px;border-radius:50%;border:1.5px solid var(--white)}
.email{position:absolute;left:714px;top:3216px;width:236px;height:44px;border-radius:22px;background:#ececf2;color:#777;font-size:11px;padding:16px 22px}
.rule{position:absolute;left:112px;top:3411px;width:976px;height:1px;background:#4c4a7c}
.copy{position:absolute;top:3438px;left:0;width:1200px;text-align:center;font-size:13px;color:var(--muted)}
</style>
</head>
<body>

<!-- HERO -->
<section class="hero">
  <div class="hero-scene" role="img" aria-label="Neon synthwave cityscape over a glowing perspective grid"></div>
  <div class="hero-sun"></div>
  <div class="brand" style="left:112px;top:64px;font-size:18px">
    <span class="brand-dot" style="width:34px;height:34px"></span>SnapNova QX
  </div>
  <nav class="nav">
    <a class="active" href="#">Home</a><a href="#">Our Booths</a><a href="#">Consumers</a><a href="#">About</a><a href="#">Customizations</a><a href="#">Contact Us</a>
  </nav>
  <div class="btn-outline" style="left:772px;top:65px;width:155px;height:39px">
    <svg width="11" height="13" viewBox="0 0 11 13"><rect x="1" y="5.5" width="9" height="7" rx="1" fill="#1ec6c6"/><path d="M3 5.5V3.5a2.5 2.5 0 0 1 5 0v2" stroke="#1ec6c6" stroke-width="1.6" fill="none"/></svg>Client Portal</div>
  <div class="btn-solid" style="left:940px;top:64px;width:148px;height:40px;font-size:14px">Find My Photos</div>
  <div class="brand" style="left:0;width:1200px;top:370px;justify-content:center;font-size:40px">
    <span class="brand-dot" style="width:44px;height:44px"></span>SnapNova QX
  </div>
  <p class="hero-text">Lorem ipsum dolor sit amet, consectetur adipiscing elit, sed do eiusmod tempor<br>incididunt ut labore et dolore magna aliqua.</p>
  <div class="btn-solid" style="left:496px;top:540px;width:208px;height:48px;border-radius:24px">BOOK ONLINE
    <svg width="16" height="16" viewBox="0 0 16 16"><circle cx="8" cy="8" r="8" fill="#fff"/><path d="M6 4.5 9.5 8 6 11.5" stroke="#1ec6c6" stroke-width="2" fill="none"/></svg></div>
</section>

<!-- BOOTHS -->
<section class="booths">
  <svg class="abs" style="left:0;top:-120px" width="1200" height="130" viewBox="0 0 1200 130"><polygon points="560,85 1200,10 1200,125" fill="#1ec6c6"/></svg>
  <svg class="abs" style="left:0;top:490px" width="1200" height="100" viewBox="0 0 1200 100"><polygon points="0,3 720,72 0,100" fill="#1ec6c6"/></svg>
</section>
<h2 class="section-title" style="top:785px">OUR BOOTHS</h2>
<div class="booth" style="left:103px;top:868px"><div class="booth-img"><div role="img" aria-label="DSLR open air photo booth kiosk" style="background:linear-gradient(160deg,#fff,#dcdde3)"></div></div><h3>DSLR Open Air Photo</h3><p>Lorem ipsum dolor consectetur adipiscing elit, sed do eiusmod tempor incididunt</p></div>
<div class="booth" style="left:360px;top:868px"><div class="booth-img"><div role="img" aria-label="Guest posing at a ring light selfie station" style="background:linear-gradient(160deg,#a07a6c,#4a3030)"></div></div><h3>Selfie Station</h3><p>Lorem ipsum dolor consectetur adipiscing elit, sed do eiusmod tempor incididunt</p></div>
<div class="booth" style="left:617px;top:868px"><div class="booth-img"><div role="img" aria-label="Drifter roaming booth with screen" style="background:linear-gradient(160deg,#6a6e78,#111)"></div></div><h3>Drifter</h3><p>Lorem ipsum dolor consectetur adipiscing elit, sed do eiusmod tempor incididunt</p></div>
<div class="booth" style="left:873px;top:868px"><div class="booth-img"><div role="img" aria-label="Pendulum Skimmer rotating booth platform" style="background:linear-gradient(160deg,#f4f4f6,#cfd1d8)"></div></div><h3>Pendulum Skimmer</h3><p>Lorem ipsum dolor consectetur adipiscing elit, sed do eiusmod tempor incididunt</p></div>

<!-- TARGETS -->
<section class="targets"></section>
<h2 class="section-title" style="top:1371px">OUR TARGETS ARE</h2>
<svg class="abs" style="left:445px;top:1480px" width="310" height="310" viewBox="0 0 310 310">
  <circle cx="155" cy="155" r="146" fill="none" stroke="#1ec6c6" stroke-width="1.5" stroke-dasharray="4 5"/>
  <circle cx="60" cy="43" r="8" fill="#1ec6c6"/><circle cx="250" cy="43" r="8" fill="#1ec6c6"/>
  <circle cx="8" cy="143" r="8" fill="#1ec6c6"/><circle cx="302" cy="143" r="8" fill="#1ec6c6"/>
  <circle cx="42" cy="255" r="8" fill="#1ec6c6"/><circle cx="268" cy="255" r="8" fill="#1ec6c6"/>
</svg>
<div class="abs" style="left:475px;top:1510px;width:250px;height:250px;border-radius:50%;background:#fff;border:5px solid var(--teal)" role="img" aria-label="White photo booth kiosk on a stand"></div>

<div class="target left" style="left:67px;top:1447px"><h4>HOLIDAY PARTIES</h4><p>Sed ut perspiciatis unde omnis iste<br>natus error sit voluptatem</p></div>
<div class="t-icon" style="left:407px;top:1446px"><svg width="32" height="32" viewBox="0 0 32 32" fill="none" stroke="#1ec6c6" stroke-width="1.6"><rect x="3" y="5" width="26" height="24" rx="2"/><path d="M3 11h26M9 2v6M23 2v6"/></svg></div>
<div class="target left" style="left:8px;top:1587px"><h4>BIRTHDAYS</h4><p>Sed ut perspiciatis unde omnis iste<br>natus error sit voluptatem</p></div>
<div class="t-icon" style="left:352px;top:1586px"><svg width="32" height="32" viewBox="0 0 32 32" fill="none" stroke="#1ec6c6" stroke-width="1.6"><rect x="4" y="16" width="24" height="12" rx="2"/><path d="M10 16V9M16 16V9M22 16V9M4 22q6 4 12 0t12 0"/></svg></div>
<div class="target left" style="left:47px;top:1725px"><h4>WEDDINGS</h4><p>Sed ut perspiciatis unde omnis iste<br>natus error sit voluptatem</p></div>
<div class="t-icon" style="left:387px;top:1724px"><svg width="32" height="32" viewBox="0 0 32 32" fill="none" stroke="#1ec6c6" stroke-width="1.6"><circle cx="11" cy="12" r="4"/><circle cx="21" cy="12" r="4"/><path d="M4 28q0-8 7-8t10 0q7 0 7 8"/></svg></div>

<div class="t-icon" style="left:717px;top:1446px"><svg width="32" height="32" viewBox="0 0 32 32" fill="none" stroke="#1ec6c6" stroke-width="1.6"><rect x="3" y="5" width="26" height="20" rx="2"/><path d="M10 29h12M16 25v4"/></svg></div>
<div class="target" style="left:809px;top:1447px"><h4>CONVENTIONS</h4><p>Sed ut perspiciatis unde omnis iste<br>natus error sit voluptatem</p></div>
<div class="t-icon" style="left:776px;top:1586px"><svg width="32" height="32" viewBox="0 0 32 32" fill="none" stroke="#1ec6c6" stroke-width="1.6"><circle cx="16" cy="10" r="7"/><circle cx="16" cy="10" r="3"/><path d="M16 13v16"/></svg></div>
<div class="target" style="left:871px;top:1587px"><h4>VIRTUAL EXPOSSS</h4><p>Sed ut perspiciatis unde omnis iste<br>natus error sit voluptatem</p></div>
<div class="t-icon" style="left:729px;top:1727px"><svg width="32" height="32" viewBox="0 0 32 32" fill="none" stroke="#1ec6c6" stroke-width="1.6"><rect x="3" y="5" width="26" height="24" rx="2"/><path d="M3 11h26M9 17h14M9 22h9"/></svg></div>
<div class="target" style="left:824px;top:1729px"><h4>COMPANY EVENTS</h4><p>Sed ut perspiciatis unde omnis iste<br>natus error sit voluptatem</p></div>

<!-- PACKAGES -->
<section class="packages"></section>
<h2 class="section-title" style="top:1963px">PACKAGES</h2>
<div class="popular">MOST POPULAR</div>
<div class="pkg" style="left:112px"><h3>Micro</h3><p class="desc">Lorem ipsum dolor sit amet,<br>consectetur elit,</p><div class="price">Free</div><div class="per">/ month</div><div class="feat">Unlimited</div><span class="try">TRY IT NOW</span></div>
<div class="pkg" style="left:445px"><h3>Small</h3><p class="desc">Lorem ipsum dolor sit amet,<br>consectetur elit,</p><div class="price">$4.99</div><div class="per">/ month</div><div class="feat">Unlimited</div><span class="try fill">TRY IT NOW</span></div>
<div class="pkg" style="left:778px"><h3>Small</h3><p class="desc">Lorem ipsum dolor sit amet,<br>consectetur elit,</p><div class="price">$4.99</div><div class="per">/ month</div><div class="feat">Unlimited</div><span class="try">TRY IT NOW</span></div>
<svg class="abs" style="left:42px;top:2244px" width="26" height="42" viewBox="0 0 26 42"><path d="M22 3 5 21l17 18" stroke="#c8cbe0" stroke-width="4" fill="none"/></svg>
<svg class="abs" style="left:1124px;top:2244px" width="26" height="42" viewBox="0 0 26 42"><path d="M4 3l17 18L4 39" stroke="#c8cbe0" stroke-width="4" fill="none"/></svg>

<!-- EXPERIENCES -->
<section class="experiences">
  <svg class="abs" style="left:0;top:0" width="1200" height="45" viewBox="0 0 1200 45"><polygon points="0,0 1200,0 1200,45 0,3" fill="#1c1656"/></svg>
</section>
<h2 class="section-title" style="top:2652px">OUR EXPERIENCES</h2>
<div class="review" style="left:110px">"Lorem ipsum dolor sit amet, consectetur adipiscing elit, sed do eiusmod tempor incididunt ut labore et dolore magna aliqua. Ut enim ad minim veniam,</div>
<div class="review" style="left:444px">"Lorem ipsum dolor sit amet, consectetur adipiscing elit, sed do eiusmod tempor incididunt ut labore et dolore magna aliqua. Ut enim ad minim veniam,</div>
<div class="review" style="left:777px;padding-top:76px">"Lorem ipsum dolor sit amet, consectetur adipiscing elit, sed do eiusmod tempor incididunt ut labore et dolore magna aliqua. Ut enim ad minim veniam,</div>
<div class="avatar" style="left:219px;top:2730px" role="img" aria-label="Reviewer portrait"></div>
<div class="avatar" style="left:553px;top:2730px" role="img" aria-label="Reviewer portrait"></div>
<div class="avatar" style="left:886px;top:2730px" role="img" aria-label="Reviewer portrait"></div>
<div class="reviewer" style="left:110px">Dr Mara Vellin</div>
<div class="reviewer" style="left:444px">Dr. Owen Trask. MD</div>
<div class="reviewer" style="left:777px">Jolie Ransome</div>
<svg width="0" height="0" style="position:absolute"><defs><polygon id="star" points="6,0 7.8,4 12,4.4 8.8,7.2 9.7,11.4 6,9.2 2.3,11.4 3.2,7.2 0,4.4 4.2,4" fill="#ffc21a"/></defs></svg>
<div class="stars" style="left:110px"><svg width="68" height="12"><use href="#star"/><use href="#star" x="14"/><use href="#star" x="28"/><use href="#star" x="42"/><use href="#star" x="56"/></svg></div>
<div class="stars" style="left:444px"><svg width="68" height="12"><use href="#star"/><use href="#star" x="14"/><use href="#star" x="28"/><use href="#star" x="42"/><use href="#star" x="56"/></svg></div>
<div class="stars" style="left:777px"><svg width="68" height="12"><use href="#star"/><use href="#star" x="14"/><use href="#star" x="28"/><use href="#star" x="42"/><use href="#star" x="56"/></svg></div>

<!-- FOOTER -->
<footer class="footer"></footer>
<div class="f-head" style="left:110px">Contact Us</div>
<div class="f-head" style="left:395px">Links</div>
<div class="f-head" style="left:538px">Vendor</div>
<div class="f-head" style="left:711px">Subscribe for Updates</div>

<svg class="abs" style="left:110px;top:3220px" width="12" height="15" viewBox="0 0 12 15"><path d="M6 15S0 8.5 0 5.5a6 6 0 0 1 12 0C12 8.5 6 15 6 15z" fill="#1ec6c6"/><circle cx="6" cy="5.5" r="2" fill="#120e3e"/></svg>
<div class="f-text" style="left:136px;top:3216px">501 E Lorem ipsum doloramet,<br>consectetur adipiscing</div>
<svg class="abs" style="left:109px;top:3284px" width="15" height="11" viewBox="0 0 15 11"><rect width="15" height="11" rx="1" fill="#1ec6c6"/><path d="M0 1l7.5 5L15 1" stroke="#120e3e" stroke-width="1.3" fill="none"/></svg>
<div class="f-text" style="left:136px;top:3279px">info@snapnovaqx.com</div>
<svg class="abs" style="left:110px;top:3323px" width="13" height="13" viewBox="0 0 13 13"><path d="M2.5 0 5 3 3.6 4.6a8 8 0 0 0 4.8 4.8L10 8l3 2.5-1.6 2.2C5.8 12.5.5 7.2.3 1.6z" fill="#1ec6c6"/></svg>
<div class="f-text" style="left:136px;top:3319px">555 014 2290</div>

<div class="f-links">Home<br>Our Booths<br>Consumers<br>About<br>Customizations<br>Contact Us</div>

<div class="vendor" style="top:3218px;font-size:15px"><span style="width:16px;height:16px;border-radius:50%;border:1.5px solid #1ec6c6"></span>bridalloom</div>
<div class="vendor" style="top:3255px;font-size:20px">grumble</div>
<div class="vendor" style="top:3298px;font-size:20px">the veil</div>

<div class="email">Emaill Address</div>
<div class="btn-solid" style="left:964px;top:3216px;width:124px;height:44px;font-size:17px">SUBMIT</div>
<svg class="abs" style="left:711px;top:3288px" width="12" height="12" viewBox="0 0 12 12"><rect x=".5" y=".5" width="11" height="11" fill="none" stroke="#9aa0c8"/><path d="M2.5 6l2.5 2.5 4.5-5" stroke="#9aa0c8" stroke-width="1.4" fill="none"/></svg>
<div class="f-text" style="left:732px;top:3285px;font-size:13px;color:#fff">Yes, Please Contact me.</div>
<div class="social" style="left:711px" aria-label="Social profile"></div>
<div class="social" style="left:756px" aria-label="Social profile"></div>
<div class="social" style="left:801px" aria-label="Social profile"></div>
<div class="social" style="left:846px" aria-label="Social profile"></div>
<div class="social" style="left:891px" aria-label="Social profile"></div>

<div class="rule"></div>
<div class="copy">© 2020 SnapNova QX. | All Rights Reserved</div>
</body>
</html>
```